Flyer Vacation Gift Certificate

I need to create a beautiful flyer 8.5 x 11 PDF format flyer design. <br/><br/>Instructions:<br/>The flyer will really be a gift voucher for a las vegas vacation getaway. So must have a Las Vegas Theme exciting fun<br/><br/>The voucher should have two modules that will be editable. <br/>Must have a "Compliments Of" area and also must have an "Exclusively For" area<br/><br/>Keep in mind that this flyer will be printed so keep that in mind :)<br/><br/>Here the is the content for the vacation voucher:<br/><br/>There is no doubt that Las Vegas is one of the hottest travel destinations around the world. In fact, some people would even go as far as<br/>saying that perhaps it is THE hottest place to visit. Enjoy up to 4 nights of resort/casino accommodations in exciting Las Vegas, NV. Millions of people travel to this exciting city each year to enjoy its thrills. Thanks to the business you received this certificate from, now you can enjoy exciting Las Vegas, NV too!<br/><br/>Features:<br/>*Travel 7 Days A Week<br/>*Stay Your Choice Of Nights (1-4 Nights)<br/>*Good For Two Adults & Two Children<br/>*Pay Just The Taxes & Fees<br/>*Multiple Travel Date Requests Allowed<br/>*Fully Transferable To Another Person<br/>*Just A 30 Days Advance Notice Required<br/>*You Will Have 12 Months To Complete Travel After Redemption<br/><br/>HOW CAN WE DO THIS?<br/><br/>We contract with the world leading hotel chains and resorts to help them fill their otherwise empty rooms.<br/><br/>We help fill empty rooms which the hotels, resorts and cruise lines turn into additional revenue from other areas of their property and future bookings.<br/><br/>Hotels rarely experience full occupancy, yet they remain open, providing rooms and services at fixed costs. So when hotels give out their rooms by partnering with marketing companies like us, they might miss out on the room fee, but they already didn't have that in the first place, at least now they have the opportunity to gain a customer for their in-house restaurants, room service, their casinos, an extra day stay, future bookings, etc.<br/><br/>VIEW ALL THE DETAILS OF THIS SPECIAL OFFER AND REDEEM ONLINE AT <br/>WWW.TOQUAMERIDIAN.EXAMPLE<br/><br/>Certificate ID # 47261-38014<br/>Expires 02/29/2020<br/><br/><br/>*terms and conditions apply see website for details<br/><br/>KEEP IN MIND THE EXAMPLES I AM UPLOADING ARE SIMPLY TO SHOW YOU THAT THEY CONTAIN THE "COMPLIMENTS OF" AND "EXCLUSIVELY FOR" ELEMENTS. THESE MUST BE INCLUDED IN NEW DESIGN. PLEASE ONLY USE THE CONTENT I PROVIDED IN BRIEF, DONT USE CONTENT FROM EXAMPLES.

Target Market(s)

CONSUMERS THAT HAVE BEEN REWARDED WITH A VACATION CERTIFICATE FOR DOING BUSINESS WITH A COMPANY.

COMPANIES USE THESE AS MARKETING INCENTIVES TO ATTRACT MORE CUSTOMERS AND TO REWARD LOYALTY, ETC.

Industry/Entity Type

Travel Industry

Colors

Designer to choose colors to be used in the design.

Requirements
Must have
• I need to create a beautiful flyer 8.5 x 11 PDF format flyer design.
• Instructions:
• The flyer will really be a gift voucher for a las vegas vacation getaway. So must have a Las Vegas Theme exciting fun
• The voucher should have two modules that will be editable.
• Must have a "Compliments Of" area and also must have an "Exclusively For" area
• Keep in mind that this flyer will be printed so keep that in mind :)
• Here the is the content for the vacation voucher:
• There is no doubt that Las Vegas is one of the hottest travel destinations around the world. In fact, some people would even go as far as
• saying that perhaps it is THE hottest place to visit. Enjoy up to 4 nights of resort/casino accommodations in exciting Las Vegas, NV. Millions of people travel to this exciting city each year to enjoy its thrills. Thanks to the business you received this certificate from, now you can enjoy exciting Las Vegas, NV too!
• Features:
• *Travel 7 Days A Week
• *Stay Your Choice Of Nights (1-4 Nights)
• *Good For Two Adults & Two Children
• *Pay Just The Taxes & Fees
• *Multiple Travel Date Requests Allowed
• *Fully Transferable To Another Person
• *Just A 30 Days Advance Notice Required
• *You Will Have 12 Months To Complete Travel After Redemption
• HOW CAN WE DO THIS?
• We contract with the world leading hotel chains and resorts to help them fill their otherwise empty rooms.
• We help fill empty rooms which the hotels, resorts and cruise lines turn into additional revenue from other areas of their property and future bookings.
• Hotels rarely experience full occupancy, yet they remain open, providing rooms and services at fixed costs. So when hotels give out their rooms by partnering with marketing companies like us, they might miss out on the room fee, but they already didn't have that in the first place, at least now they have the opportunity to gain a customer for their in-house restaurants, room service, their casinos, an extra day stay, future bookings, etc.
• VIEW ALL THE DETAILS OF THIS SPECIAL OFFER AND REDEEM ONLINE AT
• WWW.TOQUAMERIDIAN.EXAMPLE
• Certificate ID # 47261-38014
• Expires 02/29/2020
• *terms and conditions apply see website for details
• KEEP IN MIND THE EXAMPLES I AM UPLOADING ARE SIMPLY TO SHOW YOU THAT THEY CONTAIN THE "COMPLIMENTS OF" AND "EXCLUSIVELY FOR" ELEMENTS. THESE MUST BE INCLUDED IN NEW DESIGN. PLEASE ONLY USE THE CONTENT I PROVIDED IN BRIEF, DONT USE CONTENT FROM EXAMPLES.
Nice to have
• EXCITING LAS VEGAS IMAGES THAT MAKE SOMEONE WANT TO GO THERE

```html
<!DOCTYPE html>
<html lang="en">
<head>
<meta charset="utf-8">
<title>Las Vegas Vacation Certificate</title>
<link rel="stylesheet" href="https://fonts.googleapis.com/css2?family=Montserrat:wght@400;500;700;800&display=swap">
<style>
  :root {
    --stage: #3b3b3d;
    --brand-blue: #4a7cb5;
    --title-blue: #3f6fb0;
    --ink: #2a2a2a;
    --muted: #6b6b6b;
    --panel-light: #e9eaee;
    --panel-mid: #d1d2d4;
    --divider-grey: #6a6b6f;
    --list-ink: #dde7f4;
    --white: #ffffff;
  }
  * { box-sizing: border-box; margin: 0; padding: 0; }
  html, body { width: 969px; height: 1200px; overflow: hidden; background: var(--stage); }
  body { font-family: "Montserrat", Arial, sans-serif; position: relative; }

  .flyer {
    position: absolute; left: 0; top: 0;
    width: 1215px; height: 1572px;
    background: var(--white);
    transform-origin: 0 0;
    transform: translate(29.5px, 11.5px) scale(0.749);
    overflow: hidden;
  }
  .abs { position: absolute; }

  .hero-photo {
    left: 0; top: 0; width: 1215px; height: 437px;
    background:
      radial-gradient(ellipse at 60% 85%, rgba(255,196,90,.75), transparent 45%),
      radial-gradient(ellipse at 20% 75%, rgba(230,120,170,.55), transparent 35%),
      linear-gradient(180deg, #2c5c9e 0%, #5d86bd 35%, #3d4f7a 55%, #2b2a44 75%, #6a4a3a 100%);
  }

  .courtesy-card {
    left: 842px; top: 0; width: 335px; height: 287px;
    background: var(--white); text-align: center;
  }
  .courtesy-card .card-title {
    margin-top: 27px; color: var(--title-blue);
    font-size: 26px; font-weight: 500; line-height: 29px; letter-spacing: .5px;
  }
  .courtesy-card .brand-name {
    margin-top: 22px; display: flex; align-items: center; justify-content: center; gap: 10px;
    color: var(--title-blue); font-size: 30px; font-weight: 700; line-height: 40px;
  }
  .brand-name .brand-mark { width: 22px; height: 22px; background: var(--title-blue); }
  .courtesy-card .courtesy-lines {
    margin-top: 28px; color: var(--ink); font-size: 21px; line-height: 31px;
  }
  .courtesy-lines .lead { margin-bottom: 5px; }

  .intro-band {
    left: 0; top: 437px; width: 1215px; height: 121px;
    background: var(--brand-blue); color: var(--white);
    font-size: 15.5px; line-height: 19px; text-align: center;
    padding: 20px 42px 0;
  }

  .section-tab { left: 0; width: 432px; height: 54px; }
  .section-tab svg { position: absolute; left: 0; top: 0; }
  .section-tab h2 {
    position: absolute; left: 37px; top: 12px;
    color: var(--white); font-size: 23px; font-weight: 800; letter-spacing: .3px;
  }
  .tab-how { top: 601px; }
  .tab-terms { top: 916px; }

  .how-copy {
    left: 37px; top: 686px; width: 600px;
    color: var(--ink); font-size: 15.6px; line-height: 19px;
  }
  .terms-note {
    left: 37px; top: 1001px; width: 590px;
    color: var(--muted); font-size: 11.2px; line-height: 14.5px; text-transform: uppercase;
  }

  .features-panel {
    left: 673px; top: 571px; width: 542px; height: 547px;
    background: var(--brand-blue); border-bottom-left-radius: 130px;
  }
  .features-tab { left: 63px; top: 60px; width: 432px; height: 55px; }
  .features-tab svg { position: absolute; left: 0; top: 0; }
  .features-tab h2 {
    position: absolute; left: 36px; top: 12px;
    color: var(--title-blue); font-size: 23px; font-weight: 800;
  }
  .feature-list {
    left: 99px; top: 145px; width: 380px; list-style: none;
    color: var(--list-ink); font-size: 15.6px; line-height: 19px;
  }
  .feature-list li { position: relative; padding-left: 18px; }
  .feature-list li::before {
    content: ""; position: absolute; left: 0; top: 7px;
    width: 5px; height: 5px; border-radius: 50%; background: var(--white);
  }
  .redeem-info { left: 99px; top: 385px; width: 400px; color: var(--white); font-size: 15.6px; line-height: 19px; }
  .redeem-info .redeem-lead { text-transform: uppercase; margin-bottom: 19px; }
  .redeem-info .redeem-details { font-weight: 700; }

  .compliments-box {
    left: 0; top: 1163px; width: 580px; height: 409px; background: var(--panel-light);
  }
  .compliments-box h3, .exclusive-box h3 { font-size: 21px; font-weight: 500; letter-spacing: .6px; }
  .compliments-box h3 { position: absolute; left: 37px; top: 33px; color: #111; }
  .panel-divider { left: 580px; top: 1163px; }
  .exclusive-box {
    left: 621px; top: 1225px; width: 594px; height: 347px; background: var(--panel-mid);
  }
  .exclusive-box h3 { margin-top: 27px; text-align: center; color: #444; letter-spacing: 1.2px; }
</style>
</head>
<body>
  <main class="flyer">
    <div class="abs hero-photo" role="img" aria-label="Las Vegas Strip skyline at dusk with casino towers and glowing city lights"></div>

    <div class="abs courtesy-card">
      <p class="card-title">THIS CERTIFICATE IS<br>COMPLIMENTS OF</p>
      <p class="brand-name"><span class="brand-mark"></span>Lumaro Reach</p>
      <div class="courtesy-lines">
        <p class="lead">Certificate Courtesy Of</p>
        <p>Text Line 2</p>
        <p>Text Line 3</p>
      </div>
    </div>

    <p class="abs intro-band">There is no doubt that Las Vegas is one of the hottest travel destinations around the world. In fact, some people would even go as far as saying that perhaps it is THE hottest place to visit. Enjoy up to 4 nights of resort/casino accommodations in exciting Las Vegas, NV. Millions of people travel to this exciting city each year to enjoy its thrills. Thanks to the business you received this certificate from, now you can enjoy exciting Las Vegas, NV too!</p>

    <div class="abs section-tab tab-how">
      <svg width="432" height="54" viewBox="0 0 432 54"><polygon points="0,0 405,0 432,27 405,54 0,54" fill="var(--brand-blue)"/></svg>
      <h2>HOW CAN WE DO THIS?</h2>
    </div>
    <div class="abs how-copy">
      <p>We contract with the world leading hotel chains and resorts to help them fill their otherwise empty rooms. We help fill empty rooms which the hotels, resorts and cruise lines turn into additional revenue from other areas of their property and future bookings.</p>
      <p>Hotels rarely experience full occupancy, yet they remain open, providing rooms and services at fixed costs. So when hotels give out their rooms by partnering with marketing companies like us, they might miss out on the room fee, but they already didn't have that in the first place, at least now they have the opportunity to gain a customer for their in-house restaurants, room service, their casinos, an extra day stay, future bookings, etc.</p>
    </div>

    <div class="abs section-tab tab-terms">
      <svg width="432" height="54" viewBox="0 0 432 54"><polygon points="0,0 405,0 432,27 405,54 0,54" fill="var(--brand-blue)"/></svg>
      <h2>TERMS AND CONDITIONS</h2>
    </div>
    <p class="abs terms-note">Keep in mind the examples I am uploading are simply to show you that they contain the "compliments of" and "exclusively for" elements. These must be included in new design. Please only use the content I provided in brief, dont use content from examples.</p>

    <section class="abs features-panel">
      <div class="abs features-tab">
        <svg width="432" height="55" viewBox="0 0 432 55"><polygon points="0,0 408,0 432,27.5 408,55 0,55" fill="var(--white)"/></svg>
        <h2>FEATURES:</h2>
      </div>
      <ul class="abs feature-list">
        <li>Travel 7 Days A Week</li>
        <li>Stay Your Choice Of Nights (1-4 Nights)</li>
        <li>Good For Two Adults &amp; Two Children</li>
        <li>Pay Just The Taxes &amp; Fees</li>
        <li>Multiple Travel Date Requests Allowed</li>
        <li>Fully Transferable To Another Person</li>
        <li>Just A 30 Days Advance Notice Required</li>
        <li>You Will Have 12 Months To Complete Travel After Redemption</li>
      </ul>
      <div class="abs redeem-info">
        <p class="redeem-lead">View all the details of this special offer and redeem online at</p>
        <p class="redeem-details">WWW.TOQUAMERIDIAN.EXAMPLE<br>Certificate ID # 47261-38014<br>Expires 02/29/2020</p>
      </div>
    </section>

    <div class="abs compliments-box"><h3>COMPLIMENTS OF</h3></div>
    <svg class="abs panel-divider" width="41" height="409" viewBox="0 0 41 409"><polygon points="0,0 41,62 41,409 0,409" fill="var(--divider-grey)"/></svg>
    <div class="abs exclusive-box"><h3>EXCLUSIVELY FOR</h3></div>
  </main>
</body>
</html>
```